Redesign and move to Wordpress for quarvendo.com

Our website needs a redesign and at the same time we are moving it to Wordpress. Please help us with a new digital professional look and feel.

We are an Australian Software Engineering company specialising in advanced software development using in A.I., PLatform Engineering, Integration and Cloud. See the current quarvendo.com for more information about us.

```html
<!DOCTYPE html>
<html lang="en">
<head>
<meta charset="utf-8">
<title>Quarvendo — Reliable Smart Software Engineering</title>
<link href="https://fonts.googleapis.com/css2?family=Montserrat:wght@500;600;700;800&family=Lato:wght@400;700&display=swap" rel="stylesheet">
<style>
:root{
  --blue:#1e88f5;
  --blue-dark:#1670d6;
  --ink:#111318;
  --text:#3a3f4a;
  --navy:#0e1424;
  --navy-2:#1d2334;
  --pale:#dbe8f8;
  --light:#f4f6f9;
  --line:#c9d6e8;
  --white:#ffffff;
}
*{box-sizing:border-box;margin:0;padding:0}
html,body{width:1200px;height:4808px;overflow:hidden}
body{font-family:"Lato",sans-serif;color:var(--text);background:var(--white);position:relative}
.abs{position:absolute}
section,header{position:relative;width:1200px}
h1,h2,h3,.mont{font-family:"Montserrat",sans-serif}
.btn{display:inline-flex;align-items:center;gap:8px;background:var(--blue);color:#fff;font-family:"Montserrat",sans-serif;font-weight:700;font-size:14px;border-radius:3px;padding:0 18px;height:32px}
.btn-outline{background:#fff;color:var(--blue);border:2px solid var(--blue)}
.chev{width:7px;height:10px}
/* top bar */
.topbar{height:32px;background:var(--navy);color:#fff;font-size:12px}
.topbar .tag{left:112px;top:9px}
.social-top{right:112px;top:8px;display:flex;gap:14px}
.social-top span{display:flex;align-items:center;gap:5px}
.sq{width:10px;height:10px;background:#fff;border-radius:2px;display:inline-block}
/* nav */
.nav{height:95px;background:#fff}
.logo{display:flex;align-items:center;gap:12px;font-family:"Lato",sans-serif;font-size:30px;color:var(--ink);letter-spacing:1px}
.logo .mark{width:34px;height:34px;border:3px solid var(--blue);border-radius:3px}
.nav .logo{left:112px;top:28px}
.nav ul{list-style:none;display:flex;gap:30px;left:407px;top:39px;font-size:14px;color:var(--ink)}
.nav li.active{color:var(--blue)}
.nav .search{left:912px;top:39px}
.nav .btn{left:958px;top:31px;height:34px;font-size:14px}
/* hero */
.hero{height:461px;background:linear-gradient(100deg,#0c1d3a 0%,#1b4a7e 45%,#3b6891 70%,#7a8896 100%)}
.hero h1{left:112px;top:78px;color:#fff;font-size:48px;font-weight:800;line-height:52px;text-transform:uppercase}
.hero .lede{left:112px;top:258px;color:#fff;font-size:19px;line-height:25px}
.hero .btn{left:112px;top:340px;height:30px;font-size:13px}
/* about */
.about{height:423px;background:var(--light)}
.about .photo{left:112px;top:76px;width:444px;height:265px;background:linear-gradient(120deg,#4a4f57,#8b7a62 50%,#2e3845)}
.about h2{left:600px;top:72px;font-size:40px;font-weight:700;color:var(--ink)}
.about .copy{left:600px;top:139px;width:490px;font-size:14px;line-height:20px}
.checks{left:600px;top:222px;display:grid;grid-template-columns:246px 240px;row-gap:16px;font-size:15px;color:var(--ink)}
.checks li{list-style:none;display:flex;align-items:center;gap:8px}
.about .btn{left:600px;top:308px}
/* offer */
.offer{height:1029px;background:var(--pale)}
.eyebrow{width:100%;text-align:center;font-family:"Montserrat",sans-serif;font-weight:700;color:var(--blue);font-size:19px;text-transform:uppercase}
.section-title{width:100%;text-align:center;font-weight:700;font-size:40px;color:var(--ink)}
.offer .eyebrow{top:75px}
.offer .section-title{top:118px}
.cards{left:112px;top:209px;display:grid;grid-template-columns:repeat(3,300px);column-gap:38px;row-gap:39px}
.card{height:305px;background:#fff;box-shadow:0 2px 8px rgba(30,60,110,.1);text-align:center;padding:24px 20px 0;position:relative}
.card.dashed{border:2px dashed #8aa7cf;box-shadow:none}
.card svg.ico{width:64px;height:60px}
.card h3{margin-top:12px;color:var(--blue);font-size:19px;line-height:26px;font-weight:700;text-transform:uppercase}
.card p{margin-top:8px;font-size:14px;line-height:20px;color:var(--text)}
.card .btn{position:absolute;left:50%;transform:translateX(-50%);bottom:30px;height:32px;font-size:14px}
.offer .more{left:532px;top:911px;height:32px}
/* trusted */
.trusted{height:311px;background:#fff}
.trusted .lead{top:82px;width:100%;text-align:center;color:var(--blue);font-size:21px}
.brands{left:112px;top:168px;width:976px;display:flex;justify-content:space-between;align-items:center;font-family:"Lato",sans-serif;font-weight:700;font-size:36px;color:#4b5058}
.brands span{display:flex;align-items:center;gap:10px}
.brands i{width:30px;height:30px;background:#9aa0a8;display:inline-block}
/* blog */
.blog{height:989px;background:var(--navy)}
.blog .eyebrow{top:82px}
.blog .section-title{top:125px;color:#fff}
.blog-card{left:112px;top:249px;width:976px;height:651px;background:#fff}
.post{position:absolute;top:27px;width:448px}
.post .img{height:250px;background:linear-gradient(135deg,#07162d,#1b3c6a 55%,#0b1a30)}
.post h3{margin-top:24px;color:var(--blue);font-size:19px;font-weight:700;text-transform:uppercase}
.post .sub{margin-top:14px;font-size:13px;color:var(--blue)}
.post p{margin-top:12px;font-size:14px;line-height:25.5px}
.post .btn{margin-top:20px;height:32px}
.dots{position:absolute;left:0;right:0;top:614px;display:flex;justify-content:center;gap:14px}
.dots i{width:11px;height:11px;border-radius:50%;background:#c7ccd4}
.dots i:first-child{background:var(--blue)}
/* schedule */
.schedule{height:868px;background:#fff}
.schedule .eyebrow{top:80px}
.schedule .section-title{top:124px}
.booker{left:112px;top:241px;width:976px;height:591px;border:2px solid var(--line);border-radius:6px}
.host{position:absolute;left:0;top:0;width:362px;height:100%;border-right:2px solid #e3e8ef}
.avatar{left:38px;top:42px;width:66px;height:66px;border-radius:50%;background:linear-gradient(135deg,#4a3a30,#8a6c55)}
.host .name{left:132px;top:44px;color:var(--blue);font-family:"Montserrat",sans-serif;font-weight:600;font-size:25px}
.host .role{left:132px;top:82px;color:var(--blue);font-size:14px}
.host .dur{left:38px;top:156px;font-size:19px;color:var(--ink);display:flex;gap:14px;align-items:center}
.select{left:38px;top:220px;width:290px;height:42px;border:1px solid #9aa3b0;border-radius:3px;font-size:17px;color:var(--ink);padding:10px 16px}
.select .sep{position:absolute;right:44px;top:10px;width:1px;height:20px;background:#444}
.select svg{position:absolute;right:16px;top:15px}
.host .pitch{left:38px;top:316px;width:280px;font-size:19px;line-height:31px;color:var(--ink)}
.host .pitch a{color:var(--blue);text-decoration:none}
.cal{position:absolute;left:362px;top:0;width:384px}
.cal .month{left:38px;top:34px;font-family:"Montserrat",sans-serif;font-size:25px;font-weight:500;color:var(--ink)}
.cal .arrows{left:300px;top:40px;display:flex;gap:24px}
.grid{left:28px;top:86px;display:grid;grid-template-columns:repeat(7,48px);row-gap:13px;text-align:center;font-size:17px;color:var(--ink)}
.grid .wd{font-size:14px}
.grid .b{color:var(--blue)}
.grid .today{background:#cfe3fb;border-radius:50%;width:32px;height:28px;line-height:28px;margin:-5px auto 0}
.cal .note{left:38px;top:352px;width:300px;font-size:19px;line-height:31px;color:var(--ink)}
.cal .btn{left:46px;top:447px;height:44px;font-size:15px;gap:14px}
.times{position:absolute;left:746px;top:0;width:230px}
.times .date{left:20px;top:34px;font-family:"Montserrat",sans-serif;font-size:25px;font-weight:500;color:var(--ink)}
.slots{left:20px;top:89px;display:flex;flex-direction:column;gap:10px}
.slot{width:208px;height:42px;border:1.5px solid var(--line);color:var(--blue);font-size:14px;display:flex;align-items:center;justify-content:center}
.slot.sel{background:var(--blue);color:#fff;border-color:var(--blue)}
/* subscribe + footer */
.subscribe{height:261px;background:var(--navy)}
.support{left:0;top:84px;width:504px;height:123px;background:var(--navy-2);clip-path:polygon(0 0,430px 0,504px 100%,0 100%)}
.support .phone{left:112px;top:26px;display:flex;align-items:center;gap:18px;color:#fff;font-size:21px}
.support .note{left:112px;top:78px;color:#fff;font-size:14px}
.subscribe h3{left:622px;top:102px;color:#fff;font-size:30px;font-weight:700}
.subscribe .hint{left:808px;top:115px;color:#fff;font-size:15px}
.subscribe .field{left:626px;top:154px;width:296px;height:38px;border:1.5px solid #9aa3b0;border-radius:3px;color:#fff;font-size:14px;padding:10px 26px}
.subscribe .btn{left:937px;top:154px;height:38px;font-size:16px}
.footer{height:339px;background:var(--navy)}
.footer .logo{left:112px;top:60px;color:#fff;font-size:40px}
.footer .logo .mark{width:52px;height:52px;border-color:#fff}
.footer .about-text{left:112px;top:121px;width:360px;color:#fff;font-size:15px;line-height:25px}
.fcol{position:absolute;top:58px;color:#fff}
.fcol h4{font-family:"Montserrat",sans-serif;font-weight:700;font-size:25px}
.fcol ul{list-style:none;margin-top:26px;display:flex;flex-direction:column;gap:12px;font-size:15px}
.fcol.social ul{color:var(--blue);font-size:19px;gap:15px;margin-top:28px}
.fcol.social li{display:flex;align-items:center;gap:10px}
.fcol.social .sq{background:var(--blue);width:16px;height:16px}
.copyright{top:289px;width:100%;text-align:center;color:#fff;font-size:14px}
</style>
</head>
<body>
<header class="topbar">
  <span class="abs tag">Where Ideas Meet Intelligent Engineering.</span>
  <div class="abs social-top"><span><i class="sq"></i>Friendbook</span><span><i class="sq"></i>Snapgram</span><span><i class="sq"></i>WorkLink</span></div>
</header>
<header class="nav">
  <div class="abs logo"><span class="mark"></span>quarvendo</div>
  <ul class="abs"><li class="active">Home</li><li>About us</li><li>Services</li><li>Blog</li><li>Contact us</li></ul>
  <svg class="abs search" width="16" height="16" viewBox="0 0 16 16"><circle cx="6.5" cy="6.5" r="5" fill="none" stroke="#111" stroke-width="2"/><path d="M10.5 10.5l4 4" stroke="#111" stroke-width="2"/></svg>
  <span class="abs btn">Free Demo</span>
</header>

<section class="hero" role="img" aria-label="Engineers working at multi-monitor workstations in a software lab">
  <h1 class="abs">Reliable<br>Smart Software<br>Engineering</h1>
  <p class="abs lede">Innovation Starts Here<br>Custom Software for Your Unique Goals.</p>
  <span class="abs btn">Learn more <svg class="chev" viewBox="0 0 7 10"><path d="M1 1l4 4-4 4" fill="none" stroke="#fff" stroke-width="2"/></svg></span>
</section>

<section class="about">
  <div class="abs photo" role="img" aria-label="Team of developers smiling while reviewing work on a tablet and laptop"></div>
  <h2 class="abs">About Us</h2>
  <p class="abs copy">At Quarvendo, we craft bespoke software solutions that are not available on the market.Partner with us to redefine what's possible with cutting-edge technology.</p>
  <ul class="abs checks">
    <li><svg width="15" height="15" viewBox="0 0 16 16"><circle cx="8" cy="8" r="8" fill="#1e88f5"/><path d="M4.5 8.2l2.3 2.3 4.7-4.7" fill="none" stroke="#fff" stroke-width="2"/></svg>Market-leading products</li>
    <li><svg width="15" height="15" viewBox="0 0 16 16"><circle cx="8" cy="8" r="8" fill="#1e88f5"/><path d="M4.5 8.2l2.3 2.3 4.7-4.7" fill="none" stroke="#fff" stroke-width="2"/></svg>Process automation</li>
    <li><svg width="15" height="15" viewBox="0 0 16 16"><circle cx="8" cy="8" r="8" fill="#1e88f5"/><path d="M4.5 8.2l2.3 2.3 4.7-4.7" fill="none" stroke="#fff" stroke-width="2"/></svg>Legacy system enablement</li>
    <li><svg width="15" height="15" viewBox="0 0 16 16"><circle cx="8" cy="8" r="8" fill="#1e88f5"/><path d="M4.5 8.2l2.3 2.3 4.7-4.7" fill="none" stroke="#fff" stroke-width="2"/></svg>Advanced intelligent systems</li>
  </ul>
  <span class="abs btn">Learn more <svg class="chev" viewBox="0 0 7 10"><path d="M1 1l4 4-4 4" fill="none" stroke="#fff" stroke-width="2"/></svg></span>
</section>

<section class="offer">
  <p class="abs eyebrow">We Offer</p>
  <h2 class="abs section-title">Custom Solutions Tailored to Your Needs</h2>
  <div class="abs cards">
    <article class="card">
      <svg class="ico" viewBox="0 0 64 60" fill="none" stroke="#1e88f5" stroke-width="1.6"><circle cx="12" cy="10" r="4"/><circle cx="32" cy="10" r="4"/><circle cx="52" cy="10" r="4"/><circle cx="12" cy="30" r="5"/><circle cx="32" cy="30" r="5"/><circle cx="52" cy="30" r="5"/><circle cx="22" cy="50" r="4"/><circle cx="42" cy="50" r="4"/><path d="M17 30h10M37 30h10M26 50h12"/></svg>
      <h3>Enterprise Systems<br>Integration</h3>
      <p>Automate your business processes internally or externally to improve data quality and process efficiency</p>
      <span class="btn">Learn More <svg class="chev" viewBox="0 0 7 10"><path d="M1 1l4 4-4 4" fill="none" stroke="#fff" stroke-width="2"/></svg></span>
    </article>
    <article class="card dashed">
      <svg class="ico" viewBox="0 0 64 60" fill="none" stroke="#1e88f5" stroke-width="1.6"><circle cx="10" cy="30" r="5" fill="#1e88f5"/><circle cx="32" cy="12" r="4"/><circle cx="54" cy="30" r="5"/><circle cx="32" cy="48" r="4"/><circle cx="42" cy="30" r="3"/><path d="M15 30h24M10 30L32 12M32 16v12M32 44V34M45 30h4"/></svg>
      <h3>Micro<br>Services</h3>
      <p>Leverage Microservices Architecture to enable quick deployment, team productivity and more</p>
      <span class="btn btn-outline">Learn More <svg class="chev" viewBox="0 0 7 10"><path d="M1 1l4 4-4 4" fill="none" stroke="#1e88f5" stroke-width="2"/></svg></span>
    </article>
    <article class="card">
      <svg class="ico" viewBox="0 0 64 60" fill="none" stroke="#1e88f5" stroke-width="1.6"><path d="M18 36a10 10 0 0 1 2-20 13 13 0 0 1 25 2 9 9 0 0 1 1 18z"/><path d="M32 36v14M24 36v8M40 36v8"/><circle cx="32" cy="53" r="3"/><circle cx="24" cy="47" r="3"/><circle cx="40" cy="47" r="3"/></svg>
      <h3>Platform<br>Engineering</h3>
      <p>For organisations looking to manage the security and cost risks around their cloud infrastructure</p>
      <span class="btn">Learn More <svg class="chev" viewBox="0 0 7 10"><path d="M1 1l4 4-4 4" fill="none" stroke="#fff" stroke-width="2"/></svg></span>
    </article>
    <article class="card">
      <svg class="ico" viewBox="0 0 64 60" fill="none" stroke="#1e88f5" stroke-width="1.6"><rect x="20" y="4" width="24" height="10" rx="2"/><rect x="6" y="24" width="22" height="10" rx="2"/><rect x="36" y="24" width="22" height="10" rx="2" fill="#1e88f5"/><rect x="20" y="44" width="24" height="10" rx="2"/><path d="M32 14v6H17v4M32 20h15v4M17 34v5h15v5"/></svg>
      <h3>Integration Platform<br>as a Service</h3>
      <p>This is the new integration approach that enables quick, efficient and reliable enterprise systems integration</p>
      <span class="btn">Learn More <svg class="chev" viewBox="0 0 7 10"><path d="M1 1l4 4-4 4" fill="none" stroke="#fff" stroke-width="2"/></svg></span>
    </article>
    <article class="card">
      <svg class="ico" viewBox="0 0 64 60" fill="none" stroke="#1e88f5" stroke-width="1.6"><path d="M24 56V44a18 18 0 1 1 20-8v6h-6v14"/><circle cx="30" cy="18" r="3"/><circle cx="38" cy="26" r="3"/><circle cx="28" cy="30" r="3"/><path d="M30 21l-1 6M33 18l5 5"/></svg>
      <h3>Copilot /AI<br>Agents</h3>
      <p>Automate your business processes internally or externally to improve data quality and process efficiency</p>
      <span class="btn">Learn More <svg class="chev" viewBox="0 0 7 10"><path d="M1 1l4 4-4 4" fill="none" stroke="#fff" stroke-width="2"/></svg></span>
    </article>
    <article class="card">
      <svg class="ico" viewBox="0 0 64 60" fill="none" stroke="#1e88f5" stroke-width="1.6"><path d="M22 54V42a18 18 0 1 1 22-6v4h-6v14"/><circle cx="32" cy="24" r="6"/><path d="M32 14v4M32 30v4M22 24h4M38 24h4"/><path d="M10 20a22 22 0 0 1 12-14" /></svg>
      <h3>Real-Time Data<br>Stream Processing</h3>
      <p>Able to react to changing business conditions in a precise intelligent way is becoming more important.</p>
      <span class="btn">Learn More <svg class="chev" viewBox="0 0 7 10"><path d="M1 1l4 4-4 4" fill="none" stroke="#fff" stroke-width="2"/></svg></span>
    </article>
  </div>
  <span class="abs btn btn-outline more">See More <svg width="14" height="10" viewBox="0 0 14 10"><path d="M0 5h12M8 1l4 4-4 4" fill="none" stroke="#1e88f5" stroke-width="2"/></svg></span>
</section>

<section class="trusted">
  <p class="abs lead mont">Trusted by teams worldwide at innovative companies</p>
  <div class="abs brands">
    <span>Northway</span>
    <span><i></i>Corelane</span>
    <span><i></i>Brightfield</span>
    <span>Solara</span>
  </div>
</section>

<section class="blog">
  <p class="abs eyebrow">Our Blog</p>
  <h2 class="abs section-title">Updates from Our Industry</h2>
  <div class="abs blog-card">
    <article class="post" style="left:26px">
      <div class="img" role="img" aria-label="Hands holding a phone with glowing AI interface graphics"></div>
      <h3>Business Insights</h3>
      <p class="sub">How story telling heps data-driven teams succeed</p>
      <p>Winning leaders know that data alone isn't enough. It's the art of storytelling that drives sustained performance. In the spring of 2014, the Harbor City Hawks hired Dan Mercer as their head coach. Despite a star-studded roster, they hadn't won an national championship in 40 years. Mercer changed the system, combining talent with authentic storytelling.</p>
      <span class="btn">Read More <svg class="chev" viewBox="0 0 7 10"><path d="M1 1l4 4-4 4" fill="none" stroke="#fff" stroke-width="2"/></svg></span>
    </article>
    <article class="post" style="left:502px">
      <div class="img" role="img" aria-label="Hand on a laptop with floating holographic data dashboards"></div>
      <h3>Artificial Intelligence</h3>
      <p class="sub">Advancing updates on responsible AI Research</p>
      <p>A surge of generative AI models in the past year has fueled much discussion about the impact of artificial intelligence on human history. Whether exploring impressive new capabilities of large language models (LLMs) such as Model-4 or examining the spectrum of machine learning techniques already embedded in our daily lives, researchers agree on the importance of transparency.</p>
      <span class="btn">Read More <svg class="chev" viewBox="0 0 7 10"><path d="M1 1l4 4-4 4" fill="none" stroke="#fff" stroke-width="2"/></svg></span>
    </article>
    <div class="dots"><i></i><i></i><i></i><i></i><i></i></div>
  </div>
</section>

<section class="schedule">
  <p class="abs eyebrow">Let's Connect</p>
  <h2 class="abs section-title">Schedule a Consultation Now</h2>
  <div class="abs booker">
    <div class="host">
      <div class="abs avatar" role="img" aria-label="Portrait of the chief technical officer"></div>
      <p class="abs name">Quarvendo</p>
      <p class="abs role">Chief Technical Officer</p>
      <p class="abs dur"><svg width="18" height="22" viewBox="0 0 18 22"><path d="M2 1h14M2 21h14M3 1c0 6 5 7 5 10s-5 4-5 10M15 1c0 6-5 7-5 10s5 4 5 10" fill="none" stroke="#1e88f5" stroke-width="2"/></svg>30 Minutes</p>
      <div class="abs select">Australia (GMT+11)<span class="sep"></span><svg width="12" height="8" viewBox="0 0 12 8"><path d="M1 1l5 5 5-5" fill="none" stroke="#222" stroke-width="2"/></svg></div>
      <p class="abs pitch">Book an obligation free <a>consultation</a> with our Lead Technologist today for personalized <a>support</a> and <a>guidance.</a></p>
    </div>
    <div class="cal" style="height:100%">
      <p class="abs month">January</p>
      <div class="abs arrows"><svg width="10" height="16" viewBox="0 0 10 16"><path d="M8 2L2 8l6 6" fill="none" stroke="#bbb" stroke-width="2.5"/></svg><svg width="10" height="16" viewBox="0 0 10 16"><path d="M2 2l6 6-6 6" fill="none" stroke="#222" stroke-width="2.5"/></svg></div>
      <div class="abs grid">
        <span class="wd">Sun</span><span class="wd">Mon</span><span class="wd">Tue</span><span class="wd">Wed</span><span class="wd">Thu</span><span class="wd">Fri</span><span class="wd">Sat</span>
        <span></span><span></span><span></span><span>1</span><span>2</span><span>3</span><span>4</span>
        <span>5</span><span>6</span><span>7</span><span>8</span><span>9</span><span>10</span><span>11</span>
        <span class="b">12</span><span class="b">13</span><span class="b">14</span><span class="b">15</span><span class="b"><span class="today" style="display:block">16</span></span><span class="b">17</span><span class="b">18</span>
        <span class="b">19</span><span class="b">20</span><span class="b">21</span><span class="b">22</span><span class="b">23</span><span class="b">24</span><span class="b">25</span>
        <span class="b">26</span><span class="b">27</span><span class="b">28</span><span class="b">29</span><span class="b">30</span><span class="b">31</span><span></span>
      </div>
      <p class="abs note">You can choose your slot so that we can meet at your desirable and convenient timings.</p>
      <span class="abs btn">Schedule Meet <svg width="18" height="18" viewBox="0 0 18 18" fill="none" stroke="#fff" stroke-width="1.6"><rect x="2" y="3" width="14" height="13" rx="1"/><path d="M2 7h14M6 1v4M12 1v4M6 11l2 2 4-4"/></svg></span>
    </div>
    <div class="times" style="height:100%">
      <p class="abs date">Thu, Jan 16</p>
      <div class="abs slots">
        <span class="slot">10.00 AM</span><span class="slot">12.00 PM</span><span class="slot">13.30 PM</span><span class="slot sel">15.00 PM</span><span class="slot">17.30 PM</span><span class="slot">19.00 PM</span><span class="slot">20.30 PM</span><span class="slot">22.00 PM</span>
      </div>
    </div>
  </div>
</section>

<section class="subscribe">
  <div class="abs support">
    <p class="abs phone"><svg width="34" height="34" viewBox="0 0 34 34"><circle cx="17" cy="17" r="16" fill="#1e88f5"/><path d="M11 10c1-1 2-1 3 0l2 3-2 2c1 2 3 4 5 5l2-2 3 2c1 1 1 2 0 3-2 2-5 1-9-3s-5-7-4-10z" fill="#fff"/></svg>1-800-555-0142</p>
    <p class="abs note">Our Support Service is always available 24/7</p>
  </div>
  <h3 class="abs">Subscribe</h3>
  <p class="abs hint">Get the latest updates and offers</p>
  <div class="abs field">Your E-mail</div>
  <span class="abs btn">Subscribe <svg width="14" height="16" viewBox="0 0 14 16"><path d="M7 1a4 4 0 0 1 4 4v4l2 3H1l2-3V5a4 4 0 0 1 4-4zM5 13a2 2 0 0 0 4 0" fill="#fff"/></svg></span>
</section>

<footer class="footer" style="position:relative;width:1200px">
  <div class="abs logo"><span class="mark"></span>quarvendo</div>
  <p class="abs about-text">At Quarvendo, we craft bespoke software solutions that are not available on the market. Partner with us to redefine what's possible with cutting-edge technology.</p>
  <div class="fcol" style="left:547px"><h4>Explore</h4><ul><li>Home</li><li>About us</li><li>Services</li><li>Blog</li></ul></div>
  <div class="fcol" style="left:730px"><h4>Useful Links</h4><ul><li>Privacy policy</li><li>Terms of service</li><li>Cookies</li><li>Support</li></ul></div>
  <div class="fcol social" style="left:968px"><h4>Socials</h4><ul><li><i class="sq"></i>Friendbook</li><li><i class="sq"></i>Snapgram</li><li><i class="sq"></i>WorkLink</li></ul></div>
  <p class="abs copyright">© 2025 Quarvendo. All Rights Reserved.</p>
</footer>
</body>
</html>
```